Kelvo Tech Oz Business card revamp

We are looking to revamp our business card design. We are hoping to change our colours to dark navey blue, gray, white and black but are open to keeping the same if a good design is submited. We are after somthing a bit differnt not just boring business card. I have attached a copy of our current card. We Want to keep the same logo design which i have attached a few to hopfully help you in this process. We are after a design that can be personalized to separate 4 people

Colors
0455a3
ffffff
000000
cbcbcb

Requirements
Must have
• Kelvo Tech Logo, address 3/41 Mallory Court, Wexhill 4218, phone number, Name and position

```html
<!DOCTYPE html>
<html lang="en">
<head>
<meta charset="utf-8">
<title>Kelvo Tech Business Card</title>
<link rel="stylesheet" href="https://fonts.googleapis.com/css2?family=Montserrat:wght@700;800&family=Open+Sans:wght@400;600&display=swap">
<style>
  :root {
    --navy: #062066;
    --brand-blue: #0455a3;
    --accent-line: #3f7fc6;
    --white: #ffffff;
    --ink: #111111;
    --stage: #d6d6d6;
  }
  * { box-sizing: border-box; margin: 0; padding: 0; }
  html, body { width: 1200px; height: 1200px; overflow: hidden; }
  body {
    background: var(--stage);
    font-family: "Open Sans", sans-serif;
    position: relative;
  }
  .card {
    position: absolute;
    left: 180px;
    width: 840px;
    height: 480px;
    box-shadow: 0 8px 24px rgba(0,0,0,0.18);
  }
  .card-back {
    top: 90px;
    background: var(--navy);
    border: 14px solid var(--white);
    display: flex;
    align-items: center;
    justify-content: center;
  }
  .card-front {
    top: 630px;
    background: var(--white);
    border: 20px solid var(--navy);
    display: flex;
    align-items: center;
    padding: 0 60px 0 70px;
  }
  .brand {
    display: flex;
    align-items: center;
    gap: 18px;
    font-family: "Montserrat", sans-serif;
    font-weight: 800;
    letter-spacing: 0.5px;
  }
  .brand-mark {
    width: 46px; height: 46px;
    border-radius: 50%;
    flex: none;
  }
  .card-back .brand { color: var(--white); font-size: 56px; }
  .card-back .brand-mark { background: var(--white); }
  .card-front .brand { color: var(--brand-blue); font-size: 44px; }
  .card-front .brand-mark { background: var(--brand-blue); width: 38px; height: 38px; }
  .brand-block { width: 360px; }
  .divider {
    width: 2px;
    height: 210px;
    background: var(--accent-line);
    margin: 0 36px 0 24px;
  }
  .details { color: var(--ink); }
  .person-name {
    font-family: "Montserrat", sans-serif;
    font-weight: 800;
    font-size: 36px;
    color: var(--navy);
    line-height: 1;
  }
  .person-role { font-size: 18px; margin-top: 6px; }
  .contact { list-style: none; margin-top: 30px; }
  .contact li {
    display: flex;
    align-items: flex-start;
    gap: 14px;
    font-size: 20px;
    line-height: 1.25;
    margin-bottom: 12px;
  }
  .contact svg { width: 20px; height: 20px; flex: none; margin-top: 3px; fill: var(--navy); }
</style>
</head>
<body>
  <section class="card card-back" aria-label="Card back">
    <div class="brand"><span class="brand-mark"></span>Kelvo Tech</div>
  </section>

  <section class="card card-front" aria-label="Card front">
    <div class="brand-block">
      <div class="brand"><span class="brand-mark"></span>Kelvo Tech</div>
    </div>
    <div class="divider"></div>
    <div class="details">
      <div class="person-name">JOHN DOE</div>
      <div class="person-role">Director</div>
      <ul class="contact">
        <li>
          <svg viewBox="0 0 24 24" aria-hidden="true"><path d="M12 2a7 7 0 0 0-7 7c0 5 7 13 7 13s7-8 7-13a7 7 0 0 0-7-7zm0 9.5A2.5 2.5 0 1 1 12 6.5a2.5 2.5 0 0 1 0 5z"/></svg>
          <span>3/41 Mallory Court<br>Wexhill 4218</span>
        </li>
        <li>
          <svg viewBox="0 0 24 24" aria-hidden="true"><path d="M6.6 10.8a15 15 0 0 0 6.6 6.6l2.2-2.2a1 1 0 0 1 1-.25 11.4 11.4 0 0 0 3.6.57 1 1 0 0 1 1 1V20a1 1 0 0 1-1 1A17 17 0 0 1 3 4a1 1 0 0 1 1-1h3.5a1 1 0 0 1 1 1c0 1.25.2 2.45.57 3.57a1 1 0 0 1-.25 1z"/></svg>
          <span>1-234-567890</span>
        </li>
        <li>
          <svg viewBox="0 0 24 24" aria-hidden="true"><path d="M12 2a10 10 0 1 0 0 20 10 10 0 0 0 0-20zm6.9 6h-3a15.6 15.6 0 0 0-1.4-3.6A8 8 0 0 1 18.9 8zM12 4c.8 1.2 1.5 2.5 1.9 4h-3.8c.4-1.5 1.1-2.8 1.9-4zM4.3 14a8 8 0 0 1 0-4h3.4a16 16 0 0 0 0 4zm.8 2h3a15.6 15.6 0 0 0 1.4 3.6A8 8 0 0 1 5.1 16zm3-8h-3a8 8 0 0 1 4.4-3.6A15.6 15.6 0 0 0 8.1 8zM12 20c-.8-1.2-1.5-2.5-1.9-4h3.8c-.4 1.5-1.1 2.8-1.9 4zm2.3-6H9.7a14.7 14.7 0 0 1 0-4h4.6a14.7 14.7 0 0 1 0 4zm.2 5.6a15.6 15.6 0 0 0 1.4-3.6h3a8 8 0 0 1-4.4 3.6zm1.8-5.6a16 16 0 0 0 0-4h3.4a8 8 0 0 1 0 4z"/></svg>
          <span>www.companyname.com</span>
        </li>
      </ul>
    </div>
  </section>
</body>
</html>
```